Fire Risk Assessment App needs a sleek UI design

I need a sleek, modern but professional design for my 5 page Fire Risk Assessment App. Include gradient background, fire themed colours including reds, yellows, light orange and a touch of black. Design must ooze simplicity and professionalism. This is for the UK market. See attached images and word doc for more information.

Target Market(s)

General public and business owners

Industry/Entity Type

Technology / Fire Safety

Colors
00AB8E
00BBA5
67D7C9
C6EFE9
E9F9F6
59FF00
82FF00
B8FF75
E3FFCB
F4FFEA
FFC000
F8CF3A
FAE287
FDF2CF
FEFAEE
F0912C
F2A743
F7CA91
FBE8D2
FDF5EE
EE7325
F08F49
F5BC92
FAE3D3
FDF4ED
EB3D1F
EC4F4E
F09395
F8D3D4
FCEDEE

```html
<!DOCTYPE html>
<html lang="en">
<head>
<meta charset="utf-8">
<title>FireSure – Fire Risk Assessment App UI</title>
<link rel="stylesheet" href="https://fonts.googleapis.com/css2?family=Poppins:wght@300;400;500;600;700&display=swap">
<style>
:root{
  --ink:#1c1a1a;
  --muted:#8a8482;
  --line:#ead9d2;
  --red:#eb3d1f;
  --red-soft:#ec4f4e;
  --orange:#ee7325;
  --amber:#f2a743;
  --gold:#ffc000;
  --green:#00ab8e;
  --tick:#2bb34a;
  --cream:#fef7e4;
  --blush:#fce2e0;
  --paper:#fffdfa;
  --screen-bg:linear-gradient(172deg,#fef7e2 0%,#fce6e2 45%,#fde3df 60%,#fef3e1 100%);
  --cta:linear-gradient(90deg,var(--red) 0%,var(--orange) 60%,var(--amber) 100%);
  --cta-dark:linear-gradient(90deg,#141212 0%,#3a2418 45%,var(--orange) 85%,var(--amber) 100%);
}
*{box-sizing:border-box;margin:0;padding:0}
html,body{width:1200px;height:2791px;overflow:hidden;background:#fff}
body{font-family:"Poppins",sans-serif;color:var(--ink)}
.stage{position:absolute;left:0;top:0;width:1110px;height:2582px;transform:scale(1.0811);transform-origin:0 0}
.screen{position:absolute;width:184px;background:var(--screen-bg);overflow:hidden}
.t{position:absolute;white-space:nowrap;line-height:1.2}
.c{left:0;right:0;text-align:center}
.brand{position:absolute;left:0;right:0;display:flex;align-items:center;justify-content:center;gap:5px;font-size:10px;font-weight:600;color:var(--red)}
.brand i{width:16px;height:16px;border-radius:50%;background:var(--cta);display:block}
.btn{position:absolute;display:flex;align-items:center;justify-content:center;color:#fff;font-size:6.5px;border-radius:2px;background:var(--cta)}
.btn.dark{background:var(--cta-dark)}
.label{position:absolute;left:9px;font-size:6px}
.input{position:absolute;left:9px;width:166px;height:20px;background:var(--paper);border:1px solid #f3e4de;border-radius:2px;font-size:5px;color:#a9a19e;padding:6px 8px}
.avatar-ring{position:absolute;width:50px;height:50px;border-radius:50%;border:1.2px solid var(--orange);background:#fff6f0;display:flex;align-items:center;justify-content:center}
.nav{position:absolute;width:184px;height:30px}
.nav svg{position:absolute;top:5px;width:16px;height:14px}
.nav .on{position:absolute;top:3px;width:18px;height:18px}
.nav .name{position:absolute;top:20px;font-size:4.5px;transform:translateX(-50%)}
.head-icon{position:absolute;left:8px;width:12px;height:10px}
.head-title{position:absolute;left:28px;font-size:9.5px}
.plus{position:absolute;left:70px;width:42px;height:42px;border-radius:50%;background:var(--cta);box-shadow:0 4px 10px rgba(235,61,31,.25)}
.plus::before,.plus::after{content:"";position:absolute;background:#fff;left:50%;top:50%;transform:translate(-50%,-50%)}
.plus::before{width:16px;height:1.4px}.plus::after{width:1.4px;height:16px}
.start{top:115px;font-size:10.5px;font-weight:600}
.type{position:absolute;top:155px;width:62px;height:62px;border-radius:50%;background:radial-gradient(circle at 50% 45%,#c9d4dc 0%,#eef0f2 55%,#fbf4f2 100%);box-shadow:0 2px 8px rgba(0,0,0,.08)}
.type.res{background:radial-gradient(circle at 50% 50%,#5b4a48 0%,#b9a6a0 35%,#f4ecea 70%,#fbf4f2 100%)}
.type.pick{border:1.4px solid var(--amber)}
.type-name{position:absolute;top:224px;width:62px;text-align:center;font-size:8.5px}
.group{position:absolute;left:9px;width:165px;background:rgba(255,255,255,.55);border-radius:2px}
.tab{position:absolute;left:0;top:0;height:12px;display:flex;align-items:center;font-size:6px;border-bottom:1px solid var(--line);width:100%}
.tab b{width:12px;height:12px;display:flex;align-items:center;justify-content:center}
.tab span{padding:0 14px 0 6px;height:12px;line-height:12px;border:1px solid var(--line);border-bottom:0;border-radius:1px 10px 0 0}
.group .item{position:absolute;left:10px;font-size:6px;display:flex;align-items:center;gap:6px}
.dot{width:5px;height:5px;border-radius:50%;background:var(--orange)}
.ring-s{width:6px;height:6px;border-radius:50%;border:1px solid var(--ink);border-right-color:transparent}
.plan{position:absolute;width:80px;height:60px;background:var(--paper);border:1px solid #eee3df;border-radius:2px}
.plan .tag{position:absolute;left:0;top:0;width:34px;height:9px;font-size:5px;color:#fff;text-align:center;line-height:9px}
.plan .opt{position:absolute;left:8px;top:19px;font-size:5.5px}
.plan .price{position:absolute;left:8px;top:27px;font-size:10.5px;font-weight:600}
.plan .qty{position:absolute;left:8px;top:45px;font-size:4.5px}
.bubble{position:absolute;font-size:5.5px;line-height:1.35;padding:5px 8px;border-radius:4px}
.bubble.in{background:#fff;color:var(--ink)}
.bubble.out{background:linear-gradient(90deg,var(--red),var(--orange) 70%,var(--amber));color:#fff}
.time{position:absolute;font-size:5.5px}
.photo-face{position:absolute;width:22px;height:22px;border-radius:50%;background:linear-gradient(135deg,#6f4bb0,#e2b8d8)}
.card{position:absolute;left:9px;top:53px;width:166px;background:rgba(255,255,255,.55);border-radius:3px;box-shadow:0 1px 4px rgba(0,0,0,.05)}
.card .t{font-size:6px}
.card .tiny{font-size:4.5px;color:var(--muted);right:8px}
.card .ring{position:absolute;left:133px;width:20px;height:20px}
.card .rule{position:absolute;left:8px;top:87px;width:150px;height:1px;background:var(--line)}
.card .bolt{position:absolute;left:75px;top:79px;width:17px;height:17px}
.ans{position:absolute;top:143px;width:13px;height:13px}
.ans-l{position:absolute;top:159px;font-size:4.5px;color:var(--muted);transform:translateX(-50%)}
.note{position:absolute;left:8px;top:180px;width:150px;height:14px;background:#fff;border:1px solid #efe6e2;font-size:5px;color:var(--muted);text-align:center;line-height:12px}
.fuse{position:absolute;left:32px;width:102px;height:63px;background:linear-gradient(160deg,#c9c6c3,#f4f2ef 45%,#8f8b86 100%);border-radius:1px}
.save{position:absolute;left:10px;width:49px;height:13px;font-size:5px}
.next{position:absolute;left:114px;width:43px;height:13px;border:1px solid var(--red);border-radius:2px;background:#fff;font-size:5px;display:flex;align-items:center;justify-content:center;gap:3px}
.voice{position:absolute;left:8px;top:179px;width:150px;height:59px;background:#3c3b3b;border-radius:2px;color:#fff;font-size:6px;text-align:center}
.link{stroke:var(--orange);fill:none;stroke-width:1}
.conn{position:absolute;left:0;top:0;width:1110px;height:2582px;pointer-events:none}
</style>
</head>
<body>
<svg width="0" height="0" style="position:absolute">
  <symbol id="i-yes" viewBox="0 0 16 16"><circle cx="8" cy="8" r="8" fill="#2bb34a"/><path d="M4.5 8.3l2.3 2.3 4.7-5" stroke="#fff" stroke-width="1.6" fill="none"/></symbol>
  <symbol id="i-no" viewBox="0 0 16 16"><circle cx="8" cy="8" r="8" fill="#e8373a"/><path d="M5.3 5.3l5.4 5.4M10.7 5.3l-5.4 5.4" stroke="#fff" stroke-width="1.6"/></symbol>
  <symbol id="i-na" viewBox="0 0 16 16"><circle cx="8" cy="8" r="8" fill="#f5a623"/><path d="M4.8 8h6.4" stroke="#fff" stroke-width="1.8"/></symbol>
  <symbol id="i-cam" viewBox="0 0 16 16"><path d="M2 5h3l1.3-2h3.4L11 5h3v8H2z" fill="#1c1a1a"/><circle cx="8" cy="9" r="2.6" fill="#fff"/><circle cx="8" cy="9" r="1.6" fill="#1c1a1a"/></symbol>
  <symbol id="i-mic" viewBox="0 0 16 16"><rect x="5.8" y="1.5" width="4.4" height="8" rx="2.2" fill="#6e6a69"/><path d="M3.8 7.5a4.2 4.2 0 008.4 0M8 11.7v2.8M5.8 14.5h4.4" stroke="#6e6a69" stroke-width="1.1" fill="none"/></symbol>
  <symbol id="i-back" viewBox="0 0 10 10"><path d="M6.5 1.5L3 5l3.5 3.5" stroke="#1c1a1a" stroke-width="1.2" fill="none"/></symbol>
  <symbol id="i-bolt" viewBox="0 0 16 16"><circle cx="8" cy="8" r="8" fill="#141212"/><path d="M8.8 3.5L5.6 8.6h2.2L7 12.5l3.4-5.2H8.2z" fill="#ffc000"/></symbol>
  <symbol id="i-ring" viewBox="0 0 20 20"><circle cx="10" cy="10" r="8" stroke="#e7eee9" stroke-width="2.2" fill="none"/><path d="M10 2a8 8 0 11-7.6 10.5" stroke="#2bb34a" stroke-width="2.2" fill="none"/></symbol>
  <symbol id="i-user" viewBox="0 0 24 24"><circle cx="11" cy="8" r="4.2" stroke="#1c1a1a" stroke-width="1.2" fill="none"/><path d="M3.5 20c.8-4 3.8-6 7.5-6s6.2 1.6 7 4.5" stroke="#1c1a1a" stroke-width="1.2" fill="none"/><circle cx="18" cy="17.5" r="2.6" fill="#f5a623" stroke="#1c1a1a" stroke-width=".8"/></symbol>
  <symbol id="n-dash" viewBox="0 0 16 14"><path d="M2 11a6 6 0 0112 0z" fill="#bdb7b4"/><rect x="1" y="11" width="14" height="2" rx="1" fill="#bdb7b4"/></symbol>
  <symbol id="n-buy" viewBox="0 0 16 14"><rect x="2" y="6" width="12" height="7" rx="1" fill="#bdb7b4"/><rect x="4" y="2" width="8" height="3.5" rx=".5" fill="#bdb7b4"/><path d="M4 9h8" stroke="#fff" stroke-width=".8"/></symbol>
  <symbol id="n-chat" viewBox="0 0 16 14"><path d="M2 3h12v7H7l-3 2.5V10H2z" fill="#bdb7b4"/><path d="M5 6.5h6" stroke="#fff" stroke-width=".9"/></symbol>
  <symbol id="n-exit" viewBox="0 0 16 14"><rect x="3" y="1.5" width="7" height="11" rx=".5" stroke="#bdb7b4" stroke-width="1.2" fill="none"/><path d="M8 7h6.5M12.3 4.8L14.5 7l-2.2 2.2" stroke="#bdb7b4" stroke-width="1.2" fill="none"/></symbol>
  <symbol id="n-on" viewBox="0 0 18 18"><circle cx="9" cy="9" r="9" fill="#141212"/><path d="M3.5 12a5.5 5.5 0 0111 0z" fill="#ffc000"/><rect x="3" y="12" width="12" height="1.6" rx=".8" fill="#f08f49"/></symbol>
  <symbol id="n-on-buy" viewBox="0 0 18 18"><circle cx="9" cy="9" r="9" fill="#ffc000"/><rect x="4" y="7" width="10" height="6" rx="1" fill="#141212"/><rect x="6" y="4" width="6" height="2.5" fill="#141212"/></symbol>
  <symbol id="n-on-chat" viewBox="0 0 18 18"><circle cx="9" cy="9" r="9" fill="#ffc000"/><path d="M4 5h10v6H8.5L6 13v-2H4z" fill="#141212"/></symbol>
</svg>

<div class="stage">

<!-- connectors -->
<svg class="conn" viewBox="0 0 1110 2582">
  <path class="link" d="M508 610 C508 590 560 592 585 588 C598 585 600 570 603 560 C606 570 608 585 621 588 C646 592 698 590 698 610"/>
  <circle cx="508" cy="610" r="2" fill="#ee7325"/><circle cx="698" cy="610" r="2" fill="#ee7325"/>
  <path class="link" d="M583 773 H623"/><circle cx="583" cy="773" r="1.8" fill="#ee7325"/><circle cx="623" cy="773" r="1.8" fill="#eb3d1f"/>
  <path class="link" d="M470 1027 V1055 H736 V1027 M603 1055 V1085 H338 V1113"/>
  <circle cx="470" cy="1027" r="2" fill="#ee7325"/><circle cx="736" cy="1027" r="2" fill="#eb3d1f"/><circle cx="603" cy="1055" r="2" fill="#ee7325"/><circle cx="338" cy="1113" r="2" fill="#ee7325"/>
  <path class="link" d="M432 1320 H452"/><circle cx="432" cy="1320" r="1.6" fill="#ee7325"/><circle cx="452" cy="1320" r="1.6" fill="#eb3d1f"/>
  <path class="link" d="M658 1320 H678"/><circle cx="658" cy="1320" r="1.6" fill="#ee7325"/><circle cx="678" cy="1320" r="1.6" fill="#eb3d1f"/>
</svg>

<!-- Welcome -->
<section class="screen welcome" style="left:511px;top:63px;height:487px">
  <div class="brand" style="top:40px"><i></i>FireSure</div>
  <p class="t c" style="top:74px;font-size:8.6px">The Most <b style="font-weight:600">‘User Friendly’</b></p>
  <p class="t c" style="top:86px;font-size:8.6px"><b style="font-weight:600">Fire Risk Assessment App</b> Available.</p>
  <div role="img" aria-label="Stacked preview of the assessment form screen" style="position:absolute;left:37px;top:113px;width:114px;height:129px;border-radius:3px;background:linear-gradient(160deg,#ffffff 0%,#fff5ee 55%,#f7c9b3 100%);box-shadow:0 3px 10px rgba(235,61,31,.12)"></div>
  <p class="t c" style="top:260px;font-size:8.3px">Quick Tap Responses and Voice</p>
  <p class="t c" style="top:272px;font-size:8.3px">Activated Typing.</p>
  <div class="avatar-ring" style="left:67px;top:289px"><svg width="22" height="22"><use href="#i-user"/></svg></div>
  <div class="btn" style="left:41px;top:332px;width:102px;height:15px">Create a Free Account</div>
  <p class="t c" style="top:366px;font-size:8.3px">Any Responsible Person Can Do It.</p>
  <div class="avatar-ring" style="left:67px;top:381px"><svg width="22" height="22"><use href="#i-user"/></svg></div>
  <div class="btn dark" style="left:41px;top:424px;width:102px;height:16px">Customer Log in</div>
  <div style="position:absolute;left:20px;top:457px;width:144px;height:1px;background:#ead3c8"></div>
  <p class="t c" style="top:468px;font-size:5.5px">Created and endorsed by: <b style="font-weight:600">UK Fire Crews.</b></p>
</section>

<!-- Customer login -->
<section class="screen login" style="left:388px;top:619px;height:401px">
  <svg style="position:absolute;left:7px;top:41px" width="10" height="10"><use href="#i-back"/></svg>
  <div class="brand" style="top:38px"><i></i>FireSure</div>
  <p class="t c" style="top:75px;font-size:10.5px">Customer Log In</p>
  <p class="label" style="top:96px">Enter Your Email</p>
  <div class="input" style="top:110px">Enter Your Email...</div>
  <p class="label" style="top:138px">Password</p>
  <div class="input" style="top:152px">Enter Your Password</div>
  <p class="t c" style="top:180px;font-size:5px;font-weight:500">Forgot password?</p>
  <div class="btn" style="left:67px;top:207px;width:51px;height:21px;font-size:7px">Log in</div>
  <p class="t c" style="top:240px;font-size:5.5px">Don't have an account? <u style="font-weight:500">Create Account</u></p>
  <div style="position:absolute;left:0;top:322px;width:184px;height:79px;background:var(--paper);border:1px solid #eee2dd">
    <p class="t c" style="top:16px;font-size:6px;color:var(--muted)">Touch the fingerprint and login</p>
    <svg style="position:absolute;left:82px;top:36px" width="20" height="22" viewBox="0 0 20 22" fill="none" stroke="#ee7325" stroke-width="1">
      <path d="M3 7a8 8 0 0114 0M2 12a8 8 0 0116 0v3M5 19a9 9 0 01-1-6 6 6 0 0112 0v4M8 20a13 13 0 01-1-6 3 3 0 016 0v3a5 5 0 001 3M10 14v2a8 8 0 002 5"/>
    </svg>
  </div>
</section>

<!-- Create account -->
<section class="screen register" style="left:634px;top:619px;height:401px">
  <svg style="position:absolute;left:7px;top:41px" width="10" height="10"><use href="#i-back"/></svg>
  <div class="brand" style="top:38px"><i></i>FireSure</div>
  <p class="t c" style="top:75px;font-size:10.5px">Create Account</p>
  <p class="label" style="top:96px">User Name</p>
  <div class="input" style="top:110px">Enter Your Email...</div>
  <p class="label" style="top:138px">Password</p>
  <div class="input" style="top:152px">Xxx-Xxx-Xxxx</div>
  <p class="label" style="top:179px">Personal Details</p>
  <div class="input" style="top:193px">Business Name</div>
  <p class="label" style="top:221px">Upload Company Logo <span style="color:var(--muted);font-size:5px">(Optional)</span></p>
  <div class="input" style="top:234px"><svg style="position:absolute;right:7px;top:6px" width="7" height="7" viewBox="0 0 8 8" fill="none" stroke="#6e6a69" stroke-width=".9"><path d="M4 5.5V1M2 3l2-2 2 2M1 6v1h6V6"/></svg></div>
  <div class="btn" style="left:66px;top:272px;width:51px;height:21px;font-size:7px">Submit</div>
  <p class="t c" style="top:304px;font-size:5.5px">Already have an account? <u style="font-weight:500">Log In</u></p>
</section>

<!-- Dashboard empty -->
<section class="screen dash" style="left:236px;top:1121px;height:372px">
  <svg class="head-icon" style="top:29px" viewBox="0 0 16 14"><use href="#n-on"/></svg>
  <p class="head-title" style="top:28px">Dashboard</p>
  <div class="plus" style="top:63px"></div>
  <p class="t c start">Start Fire Risk Assessment</p>
</section>
<nav class="nav" style="left:236px;top:1493px">
  <svg class="on" style="left:21px"><use href="#n-on"/></svg><span class="name" style="left:30px">Dashboard</span>
  <svg style="left:63px"><use href="#n-buy"/></svg><svg style="left:104px"><use href="#n-chat"/></svg><svg style="left:144px"><use href="#n-exit"/></svg>
</nav>

<!-- Dashboard type choice -->
<section class="screen dash" style="left:462px;top:1121px;height:372px">
  <svg class="head-icon" style="top:29px" viewBox="0 0 16 14"><use href="#n-on"/></svg>
  <p class="head-title" style="top:28px">Dashboard</p>
  <div class="plus" style="top:63px"></div>
  <p class="t c start">Start Fire Risk Assessment</p>
  <svg style="position:absolute;left:54px;top:138px" width="76" height="16" viewBox="0 0 76 16"><path class="link" d="M2 15 C2 8 30 10 38 2 C46 10 74 8 74 15"/></svg>
  <div class="type" role="img" aria-label="Commercial building illustration" style="left:21px"></div>
  <div class="type res" role="img" aria-label="Residential house illustration" style="left:99px"></div>
  <p class="type-name" style="left:21px">Commercial</p>
  <p class="type-name" style="left:99px">Residential</p>
</section>
<nav class="nav" style="left:462px;top:1493px">
  <svg class="on" style="left:21px"><use href="#n-on"/></svg><span class="name" style="left:30px">Dashboard</span>
  <svg style="left:63px"><use href="#n-buy"/></svg><svg style="left:104px"><use href="#n-chat"/></svg><svg style="left:144px"><use href="#n-exit"/></svg>
</nav>

<!-- Dashboard with records -->
<section class="screen dash" style="left:688px;top:1121px;height:435px">
  <svg class="head-icon" style="top:29px" viewBox="0 0 16 14"><use href="#n-on"/></svg>
  <p class="head-title" style="top:28px">Dashboard</p>
  <div class="plus" style="top:63px"></div>
  <p class="t c start">Start Fire Risk Assessment</p>
  <svg style="position:absolute;left:54px;top:138px" width="76" height="16" viewBox="0 0 76 16"><path class="link" d="M2 15 C2 8 30 10 38 2 C46 10 74 8 74 15"/></svg>
  <div class="type pick" role="img" aria-label="Commercial building illustration" style="left:21px"></div>
  <div class="type res" role="img" aria-label="Residential house illustration" style="left:99px"></div>
  <p class="type-name" style="left:21px">Commercial</p>
  <p class="type-name" style="left:99px">Residential</p>

  <div class="group" style="top:245px;height:41px">
    <div class="tab"><b style="background:var(--tick)"><svg width="8" height="8" viewBox="0 0 16 16"><path d="M3 8.5l3.5 3.5 6.5-7" stroke="#fff" stroke-width="2.4" fill="none"/></svg></b><span style="color:var(--tick)">Complete</span></div>
    <p class="item" style="top:21px"><i class="dot"></i>Ray's Barbershop</p>
  </div>
  <div class="group" style="top:296px;height:49px">
    <div class="tab"><b style="background:#3a3a3a"><svg width="7" height="7" viewBox="0 0 8 8"><circle cx="4" cy="4" r="3" stroke="#fff" fill="none"/></svg></b><span>In Progress</span></div>
    <p class="item" style="top:21px"><i class="ring-s"></i>Elm Road School</p>
    <p class="item" style="top:33px"><i class="ring-s"></i>St Anne's Care Home</p>
  </div>
  <div class="group" style="top:358px;height:62px">
    <div class="tab"><b style="background:var(--amber)"><svg width="7" height="7" viewBox="0 0 8 8"><rect x="1" y="3" width="6" height="4" fill="#fff"/><rect x="2.5" y="1" width="3" height="1.6" fill="#fff"/></svg></b><span style="color:var(--amber)">Purchases</span></div>
    <p class="item" style="top:22px"><i class="dot"></i>Residential Fire Risk Assessment</p>
    <p class="item" style="top:34px"><i class="dot"></i>Commercial Fire Risk Assessment</p>
    <p class="item" style="top:46px"><i class="dot"></i>Commercial Fire Risk Assessment</p>
  </div>
</section>
<nav class="nav" style="left:688px;top:1556px">
  <svg class="on" style="left:21px"><use href="#n-on"/></svg><span class="name" style="left:30px">Dashboard</span>
  <svg style="left:63px"><use href="#n-buy"/></svg><svg style="left:104px"><use href="#n-chat"/></svg><svg style="left:144px"><use href="#n-exit"/></svg>
</nav>

<!-- Purchases -->
<section class="screen purchases" style="left:349px;top:1625px;height:375px">
  <svg class="head-icon" style="top:30px" viewBox="0 0 16 14"><use href="#n-buy" style="color:#000"/></svg>
  <p class="head-title" style="top:28px;left:26px">Purchases</p>
  <p class="t c" style="top:52px;font-size:9.5px">Fire Risk Assessment</p>
  <p class="t c" style="top:65px;font-size:9.5px">Payment Options</p>
  <div class="plan" style="left:9px;top:90px"><span class="tag" style="background:#8c5a2b">Bronze</span><p class="opt">Basic Option</p><p class="price">€ 19.99</p><p class="qty">1 - Fire Risk Assessment</p></div>
  <div class="plan" style="left:95px;top:90px"><span class="tag" style="background:#c9c6c4">Silver</span><p class="opt" style="color:var(--tick)">Savings Option</p><p class="price" style="color:#9d9896">€ 54.99</p><p class="qty">3 - Fire Risk Assessment</p></div>
  <div class="plan" style="left:9px;top:156px"><span class="tag" style="background:#e2bf63">Gold</span><p class="opt" style="color:var(--tick)">Savings Option</p><p class="price" style="color:#dca93a">€ 89.99</p><p class="qty">5 - Fire Risk Assessment</p></div>
  <div class="plan" style="left:95px;top:156px"><span class="tag" style="background:#f09395">Platinum</span><p class="opt" style="color:var(--tick)">Savings Option</p><p class="price" style="color:var(--red)">€ 174.99</p><p class="qty">10 - Fire Risk Assessment</p></div>
</section>
<nav class="nav" style="left:349px;top:2000px">
  <svg style="left:22px"><use href="#n-dash"/></svg>
  <svg class="on" style="left:62px"><use href="#n-on-buy"/></svg><span class="name" style="left:71px">Purchases</span>
  <svg style="left:104px"><use href="#n-chat"/></svg><svg style="left:144px"><use href="#n-exit"/></svg>
</nav>

<!-- Support -->
<section class="screen support" style="left:575px;top:1625px;height:375px">
  <svg class="head-icon" style="top:30px" viewBox="0 0 18 18"><use href="#n-on-chat"/></svg>
  <p class="head-title" style="top:28px;left:26px">Technical Support</p>
  <div class="photo-face" role="img" aria-label="Support agent photo" style="left:10px;top:56px"></div>
  <p class="bubble in" style="left:38px;top:57px;width:109px">Lorem ipsum is simply dummy?<br>printing and typesetting</p>
  <p class="time" style="left:29px;top:87px">8:07</p>
  <p class="bubble out" style="left:55px;top:107px;width:118px;padding-top:6px">Lorem ipsum is simply dummy?</p>
  <p class="time" style="right:10px;top:133px">8:10</p>
  <div class="photo-face" role="img" aria-label="Support agent photo" style="left:10px;top:152px"></div>
  <p class="bubble in" style="left:38px;top:155px;width:109px;padding-top:6px">Lorem ipsum is simply dummy?</p>
  <p class="time" style="left:29px;top:181px">8:12</p>
  <p class="bubble out" style="left:33px;top:204px;width:138px">Contrary to popular belief, lorem ipsum is<br>not simply random text</p>
  <p class="time" style="right:10px;top:239px">8:13</p>
  <div style="position:absolute;left:0;top:345px;width:184px;height:25px;background:rgba(255,255,255,.5);border-top:1px solid #f1e2dc">
    <svg style="position:absolute;left:8px;top:7px" width="9" height="9"><use href="#i-mic"/></svg>
    <p class="t" style="left:23px;top:8px;font-size:5.5px;color:var(--muted)">Type/record your response here.</p>
    <svg style="position:absolute;right:9px;top:7px" width="10" height="10" viewBox="0 0 10 10"><path d="M1 1l8 4-8 4 1.5-4z" fill="#ee7325"/></svg>
  </div>
</section>
<nav class="nav" style="left:575px;top:2000px">
  <svg style="left:22px"><use href="#n-dash"/></svg><svg style="left:63px"><use href="#n-buy"/></svg>
  <svg class="on" style="left:103px"><use href="#n-on-chat"/></svg><span class="name" style="left:112px">Support</span>
  <svg style="left:144px"><use href="#n-exit"/></svg>
</nav>

<!-- Assessment form screens -->
<section class="screen form" style="left:44px;top:2112px;height:372px">
  <svg style="position:absolute;left:7px;top:30px" width="10" height="10"><use href="#i-back"/></svg>
  <p class="t" style="left:24px;top:27px;font-size:9px">Fire Risk Assessment Form</p>
  <div class="card" style="height:301px">
    <p class="t" style="left:8px;top:6px;font-weight:500">Fire Risk Assessment</p><p class="t" style="left:8px;top:19px">Fire Hazards</p><p class="t" style="left:8px;top:32px">Sections: 7.30 / 30.00</p><p class="t" style="left:8px;top:45px">(Electronic Sources Of Ignition</p><p class="t" style="left:8px;top:58px">Clause 13 &amp; Annex XB)</p>
    <p class="t tiny" style="top:5px">Section Prog.</p><svg class="ring" style="top:16px"><use href="#i-ring"/></svg>
    <p class="t tiny" style="top:42px">Assessment Prog.</p><svg class="ring" style="top:55px"><use href="#i-ring"/></svg>
    <div class="rule"></div><svg class="bolt"><use href="#i-bolt"/></svg>
    <p class="t" style="left:8px;top:104px">Q: 7.01</p><p class="t" style="left:8px;top:114px;line-height:9px">Are reasonable measures taken to Prevent fires of<br>electrical origin?</p>
    <svg class="ans" style="left:11px"><use href="#i-yes"/></svg><svg class="ans" style="left:45px"><use href="#i-no"/></svg><svg class="ans" style="left:77px"><use href="#i-na"/></svg><svg class="ans" style="left:111px"><use href="#i-cam"/></svg><svg class="ans" style="left:142px"><use href="#i-mic"/></svg>
    <span class="ans-l" style="left:17px">(Yes)</span><span class="ans-l" style="left:51px">(No)</span><span class="ans-l" style="left:83px">(N/A)</span><span class="ans-l" style="left:117px">(Photo)</span><span class="ans-l" style="left:148px">(Mic)</span>
    <p class="note">No, electric sockets are overloaded.</p>
    <div class="fuse" role="img" aria-label="Photo of an electrical fuse board" style="top:207px"></div>
    <div class="btn save" style="top:285px">Save + Close</div><div class="next" style="top:285px">Next <span>→</span></div>
  </div>
</section>
<nav class="nav" style="left:44px;top:2484px">
  <svg class="on" style="left:21px"><use href="#n-on"/></svg><span class="name" style="left:30px">Dashboard</span>
  <svg style="left:63px"><use href="#n-buy"/></svg><svg style="left:104px"><use href="#n-chat"/></svg><svg style="left:144px"><use href="#n-exit"/></svg>
</nav>

<section class="screen form" style="left:253px;top:2112px;height:372px">
  <svg style="position:absolute;left:7px;top:30px" width="10" height="10"><use href="#i-back"/></svg>
  <p class="t" style="left:24px;top:27px;font-size:9px">Fire Risk Assessment Form</p>
  <div class="card" style="height:205px">
    <p class="t" style="left:8px;top:6px;font-weight:500">Fire Risk Assessment</p><p class="t" style="left:8px;top:19px">Fire Hazards</p><p class="t" style="left:8px;top:32px">Sections: 7.30 / 30.00</p><p class="t" style="left:8px;top:45px">(Electronic Sources Of Ignition</p><p class="t" style="left:8px;top:58px">Clause 13 &amp; Annex XB)</p>
    <p class="t tiny" style="top:5px">Section Prog.</p><svg class="ring" style="top:16px"><use href="#i-ring"/></svg>
    <p class="t tiny" style="top:42px">Assessment Prog.</p><svg class="ring" style="top:55px"><use href="#i-ring"/></svg>
    <div class="rule"></div><svg class="bolt"><use href="#i-bolt"/></svg>
    <p class="t" style="left:8px;top:104px">Q: 7.01</p><p class="t" style="left:8px;top:114px;line-height:9px">Are reasonable measures taken to Prevent fires of<br>electrical origin?</p>
    <svg class="ans" style="left:11px"><use href="#i-yes"/></svg><svg class="ans" style="left:45px"><use href="#i-no"/></svg><svg class="ans" style="left:77px"><use href="#i-na"/></svg><svg class="ans" style="left:111px"><use href="#i-cam"/></svg><svg class="ans" style="left:142px"><use href="#i-mic"/></svg>
    <span class="ans-l" style="left:17px">(Yes)</span><span class="ans-l" style="left:51px">(No)</span><span class="ans-l" style="left:83px">(N/A)</span><span class="ans-l" style="left:117px">(Photo)</span><span class="ans-l" style="left:148px">(Mic)</span>
    <div class="btn save" style="top:185px">Save + Close</div><div class="next" style="top:185px">Next <span>→</span></div>
  </div>
</section>
<nav class="nav" style="left:253px;top:2484px">
  <svg class="on" style="left:21px"><use href="#n-on"/></svg><span class="name" style="left:30px">Dashboard</span>
  <svg style="left:63px"><use href="#n-buy"/></svg><svg style="left:104px"><use href="#n-chat"/></svg><svg style="left:144px"><use href="#n-exit"/></svg>
</nav>

<section class="screen form" style="left:462px;top:2112px;height:372px">
  <svg style="position:absolute;left:7px;top:30px" width="10" height="10"><use href="#i-back"/></svg>
  <p class="t" style="left:24px;top:27px;font-size:9px">Fire Risk Assessment Form</p>
  <div class="card" style="height:228px">
    <p class="t" style="left:8px;top:6px;font-weight:500">Fire Risk Assessment</p><p class="t" style="left:8px;top:19px">Fire Hazards</p><p class="t" style="left:8px;top:32px">Sections: 7.30 / 30.00</p><p class="t" style="left:8px;top:45px">(Electronic Sources Of Ignition</p><p class="t" style="left:8px;top:58px">Clause 13 &amp; Annex XB)</p>
    <p class="t tiny" style="top:5px">Section Prog.</p><svg class="ring" style="top:16px"><use href="#i-ring"/></svg>
    <p class="t tiny" style="top:42px">Assessment Prog.</p><svg class="ring" style="top:55px"><use href="#i-ring"/></svg>
    <div class="rule"></div><svg class="bolt"><use href="#i-bolt"/></svg>
    <p class="t" style="left:8px;top:104px">Q: 7.01</p><p class="t" style="left:8px;top:114px;line-height:9px">Are reasonable measures taken to Prevent fires of<br>electrical origin?</p>
    <svg class="ans" style="left:11px"><use href="#i-yes"/></svg><svg class="ans" style="left:45px"><use href="#i-no"/></svg><svg class="ans" style="left:77px"><use href="#i-na"/></svg><svg class="ans" style="left:111px"><use href="#i-cam"/></svg><svg class="ans" style="left:142px"><use href="#i-mic"/></svg>
    <span class="ans-l" style="left:17px">(Yes)</span><span class="ans-l" style="left:51px">(No)</span><span class="ans-l" style="left:83px">(N/A)</span><span class="ans-l" style="left:117px">(Photo)</span><span class="ans-l" style="left:148px">(Mic)</span>
    <p class="note">No, electric sockets are overloaded.</p>
    <div class="btn save" style="top:208px">Save + Close</div><div class="next" style="top:208px">Next <span>→</span></div>
  </div>
</section>
<nav class="nav" style="left:462px;top:2484px">
  <svg class="on" style="left:21px"><use href="#n-on"/></svg><span class="name" style="left:30px">Dashboard</span>
  <svg style="left:63px"><use href="#n-buy"/></svg><svg style="left:104px"><use href="#n-chat"/></svg><svg style="left:144px"><use href="#n-exit"/></svg>
</nav>

<section class="screen form" style="left:671px;top:2112px;height:372px">
  <svg style="position:absolute;left:7px;top:30px" width="10" height="10"><use href="#i-back"/></svg>
  <p class="t" style="left:24px;top:27px;font-size:9px">Fire Risk Assessment Form</p>
  <div class="card" style="height:276px">
    <p class="t" style="left:8px;top:6px;font-weight:500">Fire Risk Assessment</p><p class="t" style="left:8px;top:19px">Fire Hazards</p><p class="t" style="left:8px;top:32px">Sections: 7.30 / 30.00</p><p class="t" style="left:8px;top:45px">(Electronic Sources Of Ignition</p><p class="t" style="left:8px;top:58px">Clause 13 &amp; Annex XB)</p>
    <p class="t tiny" style="top:5px">Section Prog.</p><svg class="ring" style="top:16px"><use href="#i-ring"/></svg>
    <p class="t tiny" style="top:42px">Assessment Prog.</p><svg class="ring" style="top:55px"><use href="#i-ring"/></svg>
    <div class="rule"></div><svg class="bolt"><use href="#i-bolt"/></svg>
    <p class="t" style="left:8px;top:104px">Q: 7.01</p><p class="t" style="left:8px;top:114px;line-height:9px">Are reasonable measures taken to Prevent fires of<br>electrical origin?</p>
    <svg class="ans" style="left:11px"><use href="#i-yes"/></svg><svg class="ans" style="left:45px"><use href="#i-no"/></svg><svg class="ans" style="left:77px"><use href="#i-na"/></svg><svg class="ans" style="left:111px"><use href="#i-cam"/></svg><svg class="ans" style="left:142px"><use href="#i-mic"/></svg>
    <span class="ans-l" style="left:17px">(Yes)</span><span class="ans-l" style="left:51px">(No)</span><span class="ans-l" style="left:83px">(N/A)</span><span class="ans-l" style="left:117px">(Photo)</span><span class="ans-l" style="left:148px">(Mic)</span>
    <div class="fuse" role="img" aria-label="Photo of an electrical fuse board" style="top:179px"></div>
    <div class="btn save" style="top:257px">Save + Close</div><div class="next" style="top:257px">Next <span>→</span></div>
  </div>
</section>
<nav class="nav" style="left:671px;top:2484px">
  <svg class="on" style="left:21px"><use href="#n-on"/></svg><span class="name" style="left:30px">Dashboard</span>
  <svg style="left:63px"><use href="#n-buy"/></svg><svg style="left:104px"><use href="#n-chat"/></svg><svg style="left:144px"><use href="#n-exit"/></svg>
</nav>

<section class="screen form" style="left:880px;top:2112px;height:372px">
  <svg style="position:absolute;left:7px;top:30px" width="10" height="10"><use href="#i-back"/></svg>
  <p class="t" style="left:24px;top:27px;font-size:9px">Fire Risk Assessment Form</p>
  <div class="card" style="height:274px">
    <p class="t" style="left:8px;top:6px;font-weight:500">Fire Risk Assessment</p><p class="t" style="left:8px;top:19px">Fire Hazards</p><p class="t" style="left:8px;top:32px">Sections: 7.30 / 30.00</p><p class="t" style="left:8px;top:45px">(Electronic Sources Of Ignition</p><p class="t" style="left:8px;top:58px">Clause 13 &amp; Annex XB)</p>
    <p class="t tiny" style="top:5px">Section Prog.</p><svg class="ring" style="top:16px"><use href="#i-ring"/></svg>
    <p class="t tiny" style="top:42px">Assessment Prog.</p><svg class="ring" style="top:55px"><use href="#i-ring"/></svg>
    <div class="rule"></div><svg class="bolt"><use href="#i-bolt"/></svg>
    <p class="t" style="left:8px;top:104px">Q: 7.01</p><p class="t" style="left:8px;top:114px;line-height:9px">Are reasonable measures taken to Prevent fires of<br>electrical origin?</p>
    <svg class="ans" style="left:11px"><use href="#i-yes"/></svg><svg class="ans" style="left:45px"><use href="#i-no"/></svg><svg class="ans" style="left:77px"><use href="#i-na"/></svg><svg class="ans" style="left:111px"><use href="#i-cam"/></svg><svg class="ans" style="left:142px"><use href="#i-mic"/></svg>
    <span class="ans-l" style="left:17px">(Yes)</span><span class="ans-l" style="left:51px">(No)</span><span class="ans-l" style="left:83px">(N/A)</span><span class="ans-l" style="left:117px">(Photo)</span><span class="ans-l" style="left:148px">(Mic)</span>
    <div class="voice">
      <p class="t c" style="top:12px">Lorem ipsum dammy work <span style="color:#9b9a9a">thinking</span></p>
      <svg style="position:absolute;left:65px;top:31px" width="20" height="16" viewBox="0 0 20 16" stroke="#fff" stroke-width="1"><path d="M2 6v4M5 4v8M8 1v14M11 3v10M14 5v6M17 7v2"/></svg>
    </div>
    <div class="btn save" style="top:253px">Save + Close</div><div class="next" style="top:253px">Next <span>→</span></div>
  </div>
</section>
<nav class="nav" style="left:880px;top:2484px">
  <svg class="on" style="left:21px"><use href="#n-on"/></svg><span class="name" style="left:30px">Dashboard</span>
  <svg style="left:63px"><use href="#n-buy"/></svg><svg style="left:104px"><use href="#n-chat"/></svg><svg style="left:144px"><use href="#n-exit"/></svg>
</nav>

</div>
</body>
</html>
```